Graphic to hang inside of fitness studio

This graphic will be printed on vinyl and hung inside of a boutique fitness studio for 2019. Graphic should read YEAR OF POSSIBILITIES.

2018 was called Year of Living Well. We would like something on trend for 2019 to hang within the studio as our 2019 Mantra. It is not a logo but for internal use. I've attached our logo here and the website is www.kestrelmovehall.com for additional reference. Thank you.

Target Market(s)

25 to 45 women

Industry/Entity Type

Fitness

Colors

Designer to choose colors to be used in the design.

Requirements
Must have
• On trend for 2019. (no people in image)
• Year of Possibilities in trendy font.
• Easy to read.
• Need text only.
• Do not need graphic images.
Nice to have
• Tintorell colours for 2019
• 2019 design trends for background
Should not have
• Male dominate colour or masculine traits.
• Photos of fitness.
• Photos of people.
• Photos of equipment.

```html
<!DOCTYPE html>
<html lang="en">
<head>
<meta charset="utf-8">
<title>Year of Possibilities — 2019 Studio Mantra</title>
<link rel="stylesheet" href="https://fonts.googleapis.com/css2?family=Lato:wght@400;700&family=Playfair+Display:ital,wght@1,700&display=swap">
<style>
  :root {
    --water-deep: #06363a;
    --water-mid: #0b5a5c;
    --water-bright: #14807c;
    --water-glint: #1fa39a;
    --text-white: #ffffff;
  }
  html, body {
    margin: 0;
    padding: 0;
    width: 1200px;
    height: 600px;
    overflow: hidden;
    background: var(--water-deep);
  }
  .mantra-banner {
    position: relative;
    width: 1200px;
    height: 600px;
    overflow: hidden;
  }
  .water-backdrop {
    position: absolute;
    inset: 0;
    background:
      radial-gradient(ellipse 420px 260px at 560px 470px, rgba(31,163,154,0.45), transparent 70%),
      radial-gradient(ellipse 500px 200px at 980px 420px, rgba(20,128,124,0.35), transparent 70%),
      radial-gradient(ellipse 380px 220px at 200px 120px, rgba(20,128,124,0.35), transparent 70%),
      linear-gradient(160deg, var(--water-mid) 0%, var(--water-deep) 45%, var(--water-mid) 75%, var(--water-bright) 100%);
  }
  .mantra-line {
    position: absolute;
    margin: 0;
    color: var(--text-white);
    line-height: 1;
    white-space: nowrap;
  }
  .mantra-year {
    top: 50px;
    right: 48px;
    font-family: "Lato", sans-serif;
    font-weight: 400;
    font-size: 111px;
    letter-spacing: 2px;
  }
  .mantra-of {
    font-family: "Playfair Display", serif;
    font-style: italic;
    font-weight: 700;
    font-size: 96px;
    letter-spacing: 0;
    margin-left: 14px;
  }
  .mantra-possibilities {
    top: 207px;
    right: 72px;
    font-family: "Lato", sans-serif;
    font-weight: 700;
    font-size: 105px;
    letter-spacing: 3px;
  }
</style>
</head>
<body>
  <main class="mantra-banner">
    <div class="water-backdrop" role="img" aria-label="Photograph of rippling turquoise water with an open hand resting at the surface holding a seashell"></div>
    <h1 class="mantra-heading">
      <span class="mantra-line mantra-year">YEAR<span class="mantra-of">of</span></span>
      <span class="mantra-line mantra-possibilities">POSSIBILITIES.</span>
    </h1>
  </main>
</body>
</html>
```